Updated Business Card for Optometry Practice

We're a growing optometry practice that is moving to a beautiful new office and we want to update our business card. We just updated our logo so the new card should reflect the new logo. Our practice continually invests in state of the art instruments to help us provide eye care that is thorough, comfortable, efficient and educational.

I've attached our current card and logo. You can reference this for the information I would like on the card. The tag line on the back is "We're changing the way you see."

Upon completion of this project we will need (amongst other formats) Photoshop files of the card so I can change employee names to print cards for each employee.

```html
<!DOCTYPE html>
<html lang="en">
<head>
<meta charset="utf-8">
<title>Brookmere Family Eyecare – Business Card</title>
<link href="https://fonts.googleapis.com/css2?family=Montserrat:wght@400;500&family=Open+Sans:wght@400;600;700&display=swap" rel="stylesheet">
<style>
  :root {
    --navy: #13284f;
    --gold: #d8b232;
    --white: #ffffff;
    --stage: #3a3a3a;
  }
  * { box-sizing: border-box; margin: 0; padding: 0; }
  html, body { width: 1200px; height: 900px; overflow: hidden; }
  body {
    background: var(--stage);
    font-family: "Open Sans", Arial, sans-serif;
    display: flex;
    align-items: center;
    justify-content: space-evenly;
  }
  .card {
    position: relative;
    width: 525px;
    height: 300px;
    background: var(--navy);
    color: var(--white);
    overflow: hidden;
  }

  /* Contact side */
  .card-front .brand {
    position: absolute;
    left: 34px;
    top: 30px;
    font-weight: 600;
    color: var(--white);
    line-height: 1.15;
  }
  .card-front .brand-name { font-size: 30px; letter-spacing: 0.5px; display: block; }
  .card-front .brand-sub { font-size: 12px; letter-spacing: 5px; display: block; }

  .contact {
    position: absolute;
    left: 34px;
    top: 118px;
  }
  .person {
    position: relative;
    padding-left: 20px;
  }
  .person::before {
    content: "";
    position: absolute;
    left: 0; top: 3px;
    width: 10px; height: 26px;
    background: var(--gold);
  }
  .person-name { font-size: 20px; font-weight: 700; line-height: 1.2; }
  .person-role { font-size: 11px; color: var(--gold); }
  .practice { margin-top: 10px; font-size: 11.5px; color: var(--gold); }
  .address { font-size: 11px; line-height: 1.45; }
  .links { list-style: none; margin-top: 8px; font-size: 11px; line-height: 1.75; }
  .links li { display: flex; align-items: center; gap: 7px; }
  .icon {
    width: 13px; height: 13px;
    border-radius: 50%;
    background: var(--gold);
    display: inline-flex;
    align-items: center;
    justify-content: center;
  }
  .icon svg { width: 8px; height: 8px; }

  /* Tagline side */
  .card-back {
    display: flex;
    flex-direction: column;
    justify-content: center;
    padding-left: 60px;
  }
  .card-back .brand { font-weight: 600; line-height: 1.15; }
  .card-back .brand-name { font-size: 52px; letter-spacing: 1px; display: block; }
  .card-back .brand-sub { font-size: 20px; letter-spacing: 9px; display: block; margin-top: 4px; }
  .tagline {
    margin-top: 22px;
    font-family: "Montserrat", Arial, sans-serif;
    font-weight: 500;
    font-size: 25px;
  }
</style>
</head>
<body>

  <section class="card card-front">
    <div class="brand">
      <span class="brand-name">BROOKMERE</span>
      <span class="brand-sub">FAMILY EYECARE</span>
    </div>

    <div class="contact">
      <div class="person">
        <div class="person-name">Daniel Marsh, OD</div>
        <div class="person-role">Optometrist</div>
      </div>
      <div class="practice">Brookmere Family Eyecare</div>
      <div class="address">2870 Linden Park Way #210<br>Westvale, MO 63099</div>
      <ul class="links">
        <li>
          <span class="icon"><svg viewBox="0 0 10 10"><path d="M2 1 L4 1 L4.6 3 L3.6 3.8 Q4.6 5.6 6.2 6.4 L7 5.4 L9 6 L9 8 Q8 9 6.5 8.6 Q2.5 7 1.2 3 Q1 1.8 2 1 Z" fill="#13284f"/></svg></span>
          (555) 018-2046
        </li>
        <li>
          <span class="icon"><svg viewBox="0 0 10 10"><rect x="1" y="2.5" width="8" height="5.5" fill="none" stroke="#13284f" stroke-width="1.2"/><path d="M1 2.5 L5 5.8 L9 2.5" fill="none" stroke="#13284f" stroke-width="1.2"/></svg></span>
          dan@brookmereeyecare.com
        </li>
        <li>
          <span class="icon"><svg viewBox="0 0 10 10"><circle cx="5" cy="5" r="3.8" fill="none" stroke="#13284f" stroke-width="1.1"/><path d="M1.2 5 H8.8 M5 1.2 Q2.8 5 5 8.8 M5 1.2 Q7.2 5 5 8.8" fill="none" stroke="#13284f" stroke-width="0.9"/></svg></span>
          www.brookmereeyecare.com
        </li>
      </ul>
    </div>
  </section>

  <section class="card card-back">
    <div class="brand">
      <span class="brand-name">BROOKMERE</span>
      <span class="brand-sub">FAMILY EYECARE</span>
    </div>
    <p class="tagline">We're changing the way you see</p>
  </section>

</body>
</html>
```